TR & Groundworks
Landscaping
TR & Groundworks - Utilities
Creative Brief
Professional
Dennis Holloway
Brisk Meadow Cooling and Yardcraft LLP
P.O. Box 618207 Christiansted, St. Croix 00822
Briskmeadowcoolingandyardcraft@mailvessel.com
Mona Fairweather is the Co-Owner name needs to be on card also

```html
<!DOCTYPE html>
<html lang="en">
<head>
<meta charset="utf-8">
<title>Brisk Meadow – Business Cards</title>
<link href="https://fonts.googleapis.com/css2?family=PT+Sans:wght@400;700&display=swap" rel="stylesheet">
<style>
  :root {
    --page: #ffffff;
    --ink: #1d3f8f;
    --ink-soft: #2a4a99;
    --blue-deep: #0b3f9a;
    --blue-mid: #1f78d1;
    --blue-light: #5fb3ee;
    --green-lime: #b6d632;
    --green-mid: #6fb43f;
    --green-deep: #2f8f3a;
    --grey-light: #f4f4f4;
    --grey-mid: #b9b9b9;
    --frame: #9a9a9a;
  }
  html, body {
    margin: 0;
    padding: 0;
    width: 1200px;
    height: 1062px;
    overflow: hidden;
    background: var(--page);
    font-family: "PT Sans", Arial, sans-serif;
  }
  .sheet {
    position: relative;
    width: 1200px;
    height: 1062px;
  }
  .card {
    position: absolute;
    width: 565px;
    height: 322px;
    box-sizing: border-box;
    border: 1px solid var(--frame);
    overflow: hidden;
  }
  .card--front-a { left: 35px; top: 35px; background: #fff; }
  .card--back-green {
    left: 620px; top: 35px;
    background: linear-gradient(90deg, var(--green-deep) 0%, var(--green-mid) 45%, var(--green-lime) 100%);
  }
  .card--front-b { left: 35px; top: 380px; height: 328px; background: #fff; }
  .card--back-grey {
    left: 620px; top: 380px; height: 328px;
    background: linear-gradient(90deg, var(--grey-mid) 0%, var(--grey-light) 50%, var(--grey-mid) 100%);
  }
  .card--back-blue {
    left: 322px; top: 732px; width: 562px;
    background: radial-gradient(circle at 50% 50%, var(--blue-light) 0%, var(--blue-mid) 35%, var(--blue-deep) 100%);
  }
  .card__art {
    position: absolute;
    inset: 0;
    width: 100%;
    height: 100%;
  }
  .brand-tag {
    position: absolute;
    left: 22px;
    top: 22px;
    width: 236px;
    height: 72px;
    background: #fff;
    border: 2px solid var(--blue-mid);
    box-sizing: border-box;
    display: flex;
    align-items: center;
    gap: 10px;
    padding: 0 12px;
  }
  .brand-tag__dot {
    width: 40px;
    height: 40px;
    border-radius: 50%;
    background: var(--blue-mid);
    flex: none;
  }
  .brand-tag__name {
    font-weight: 700;
    font-size: 27px;
    color: var(--blue-deep);
    white-space: nowrap;
  }
  .contact {
    position: absolute;
    left: 22px;
    color: var(--ink);
  }
  .contact__name {
    font-size: 26px;
    margin: 0 0 16px;
    font-weight: 400;
  }
  .contact__lines {
    margin: 0;
    font-size: 15px;
    line-height: 19px;
    color: var(--ink-soft);
  }
  .contact__email {
    font-size: 11.5px;
    white-space: nowrap;
  }
  .card--front-a .contact { top: 140px; }
  .card--front-b .contact { top: 118px; }
  .card--front-b .contact__name { font-size: 30px; margin-bottom: 26px; }
  .card--front-b .contact__lines { font-size: 17px; line-height: 22px; }
  .card--front-b .contact__email { font-size: 17px; }
  .emblem {
    position: absolute;
    left: 50%;
    top: 50%;
    transform: translate(-50%, -50%);
    display: flex;
    align-items: center;
    gap: 14px;
  }
  .emblem__dot {
    width: 56px;
    height: 56px;
    border-radius: 50%;
    background: var(--blue-deep);
    flex: none;
  }
  .emblem__name {
    font-weight: 700;
    font-size: 38px;
    color: #ffffff;
    white-space: nowrap;
  }
  .card--back-grey .emblem__name { color: var(--blue-deep); }
</style>
</head>
<body>
<main class="sheet">

  <section class="card card--front-a" aria-label="Business card front, version one">
    <svg class="card__art" viewBox="0 0 565 322" preserveAspectRatio="none" aria-hidden="true">
      <defs>
        <linearGradient id="sweepBlue" x1="0" y1="0" x2="1" y2="1">
          <stop offset="0" stop-color="#5fb3ee"/>
          <stop offset="0.5" stop-color="#1f78d1"/>
          <stop offset="1" stop-color="#0b3f9a"/>
        </linearGradient>
      </defs>
      <path d="M300 0 L565 0 L565 322 L392 322 C320 250 262 110 300 0 Z" fill="url(#sweepBlue)"/>
      <path d="M310 0 C274 110 332 250 402 322" fill="none" stroke="#ffffff" stroke-width="6"/>
    </svg>
    <div class="brand-tag">
      <span class="brand-tag__dot"></span>
      <span class="brand-tag__name">Brisk Meadow</span>
    </div>
    <div class="contact">
      <h2 class="contact__name">Mona Fairweather</h2>
      <p class="contact__lines">
        P.O. Box 618207<br>
        Christiansted, St. Croix 00822<br>
        Phone: 340-555-0190<br>
        Cell: 340-555-0147<br>
        <span class="contact__email">Email: Briskmeadowcoolingandyardcraft@mailvessel.com</span><br>
        License No.: 472961
      </p>
    </div>
  </section>

  <section class="card card--back-green" aria-label="Business card back, green">
    <div class="emblem">
      <span class="emblem__dot"></span>
      <span class="emblem__name">Brisk Meadow</span>
    </div>
  </section>

  <section class="card card--front-b" aria-label="Business card front, version two">
    <svg class="card__art" viewBox="0 0 565 328" preserveAspectRatio="none" aria-hidden="true">
      <defs>
        <linearGradient id="edgeBlue" x1="0" y1="0" x2="1" y2="1">
          <stop offset="0" stop-color="#5fb3ee"/>
          <stop offset="0.55" stop-color="#1f78d1"/>
          <stop offset="1" stop-color="#0b3f9a"/>
        </linearGradient>
      </defs>
      <path d="M420 0 L565 0 L565 328 L505 328 C540 220 525 80 420 0 Z" fill="url(#edgeBlue)"/>
      <path d="M408 0 C512 80 528 220 492 328" fill="none" stroke="#8cc63f" stroke-width="5"/>
    </svg>
    <div class="brand-tag">
      <span class="brand-tag__dot"></span>
      <span class="brand-tag__name">Brisk Meadow</span>
    </div>
    <div class="contact">
      <h2 class="contact__name">Mona Fairweather</h2>
      <p class="contact__lines">
        P.O. Box 618207<br>
        Christiansted, St. Croix 00822<br>
        Phone: 340-555-0190<br>
        Cell: 340-555-0147<br>
        <span class="contact__email">Email: Briskmeadowcoolingandyardcraft@mailvessel.com</span><br>
        License No.: 472961
      </p>
    </div>
  </section>

  <section class="card card--back-grey" aria-label="Business card back, grey">
    <div class="emblem">
      <span class="emblem__dot"></span>
      <span class="emblem__name">Brisk Meadow</span>
    </div>
  </section>

  <section class="card card--back-blue" aria-label="Business card back, blue">
    <div class="emblem">
      <span class="emblem__dot"></span>
      <span class="emblem__name">Brisk Meadow</span>
    </div>
  </section>

</main>
</body>
</html>
```